Utility Software Company Needs a Business Flyer

We need a business flyer to promote one of our Services. The MBA Department is a Service within our company and it is basically Managed Backoffice Administration. MBA provides services that lighten the workload for our clients. MBA has a team of professionals who specialize in data processing, bill processing, research, customer support, and security of financial data. We remove the burden of in house billing and payment processing.

Target Market(s)

New and existing utility customers

Industry/Entity Type

Public Utility

Font styles to use
Serif

Colors
ffcf3e
3277b5
85cae6

Requirements
Must have
• The company name - KLT, Inc.
• Logo
• Tagline
• Address - 48710 Brimley Lane, Houston, TX 77093
• Phone: 713-846-2059
• Email: sales@kltzo.com
• Website - www.kltzo.com
• Contact a Sales Associate for more information
• Diverse images of people

```html
<!DOCTYPE html>
<html lang="en">
<head>
<meta charset="utf-8">
<title>KLT, Inc. – MBA Data Processing &amp; Posting Flyer</title>
<link rel="stylesheet" href="https://fonts.googleapis.com/css2?family=Libre+Baskerville:wght@400;700&family=Lato:wght@400;700;900&display=swap">
<style>
:root{
  --yellow:#ffcf3e;
  --blue:#3277b5;
  --sky:#85cae6;
  --sky-soft:#d4ecf8;
  --navy:#1f4f8f;
  --ink:#2e2e2e;
  --grey-band:#efefef;
  --backdrop:#e4e1dc;
}
*{margin:0;padding:0;box-sizing:border-box}
html,body{width:1200px;height:903px;overflow:hidden;background:var(--backdrop)}
body{position:relative;font-family:"Lato",Arial,sans-serif;color:var(--ink)}
.page{position:absolute;top:142px;width:516px;height:665px;background:#fff;box-shadow:0 4px 14px rgba(0,0,0,.25);overflow:hidden}
.page--front{left:62px}
.page--back{left:622px}
.abs{position:absolute}

/* front header */
.brand{left:64px;top:34px;display:flex;align-items:center;gap:8px}
.brand__mark{width:12px;height:12px;border-radius:50%;background:var(--yellow)}
.brand__name{font-family:"Lato",sans-serif;font-weight:900;font-size:24px;color:var(--blue);letter-spacing:.5px}
.tagline{left:157px;top:37px;font-family:"Lato",sans-serif;font-weight:700;font-size:20px;color:var(--navy)}
.since{left:392px;top:61px;font-size:6px;font-weight:700;color:var(--navy)}
.hero-photo{left:0;top:82px;width:516px;height:271px;background:linear-gradient(135deg,#dfe7f0 0%,#a9c4e0 40%,#5f8fc6 75%,#3d6eb0 100%)}
.hero-band{left:0;top:353px;width:516px;height:86px;background:var(--blue);text-align:center}
.hero-band h1{font-family:"Libre Baskerville",Georgia,serif;font-weight:700;font-size:23px;color:var(--yellow);margin-top:20px;letter-spacing:.3px}
.hero-band p{font-family:"Libre Baskerville",Georgia,serif;font-weight:700;font-size:12.5px;color:#fff;margin-top:7px}
.intro-title{left:0;top:446px;width:516px;text-align:center;font-family:"Libre Baskerville",Georgia,serif;font-weight:700;font-size:13px;line-height:18px;color:var(--ink)}
.intro-title span{color:var(--blue)}
.body-col{top:493px;width:218px;font-size:7.7px;line-height:10px;text-align:justify}
.body-col p+p{margin-top:10px}
.body-col--a{left:26px}
.body-col--b{left:271px}

/* footer */
.footer{left:0;top:631px;width:516px;height:34px}
.footer__yellow{left:0;top:0;width:400px;height:26px;background:var(--yellow);clip-path:polygon(0 0,100% 0,96% 100%,0 100%)}
.footer__blue{left:0;top:26px;width:516px;height:8px;background:var(--blue)}
.footer__phone-block{left:388px;top:0;width:128px;height:34px;background:var(--blue);clip-path:polygon(10% 0,100% 0,100% 100%,0 100%)}
.footer__item{top:7px;display:flex;align-items:center;gap:4px;font-size:8px;color:var(--ink)}
.footer__item svg{width:8px;height:8px;fill:var(--blue)}
.footer__phone{left:402px;top:5px;display:flex;align-items:center;gap:5px;font-size:10.5px;font-weight:700;color:#fff}
.footer__phone svg{width:10px;height:10px;fill:#fff}

/* back page */
.section-title{height:18px;background:var(--blue);color:#fff;font-family:"Lato",sans-serif;font-weight:700;font-size:15px;line-height:18px;text-align:center;border:1px solid var(--navy)}
.section-title span{color:var(--yellow)}
.services-title{left:158px;top:25px;width:201px}
.adv-title{left:145px;top:430px;width:229px}
.lead{left:31px;top:57px;display:flex;align-items:center;gap:5px;font-size:9.5px;font-weight:700;color:var(--blue)}
.tick{width:8px;height:8px;flex:none}
.channel-bar{left:28px;width:460px;height:14px;border-bottom:1px solid var(--yellow)}
.channel-bar__icon{position:absolute;left:0;top:0;width:13px;height:13px;background:var(--blue);border:1px solid var(--yellow)}
.channel-bar__tab{position:absolute;left:16px;top:0;height:13px;padding:0 14px 0 9px;background:var(--blue);color:#fff;font-size:9.5px;font-weight:700;line-height:13px;clip-path:polygon(0 0,100% 0,92% 100%,0 100%)}
.channel-bar__slash{position:absolute;top:0;width:4px;height:13px;background:var(--yellow);transform:skewX(20deg)}
.lockbox{left:43px;top:99px;width:446px;font-size:7.7px;line-height:10px;text-align:justify}
.grey-band{left:0;top:150px;width:516px;height:128px;background:var(--grey-band)}
.item{width:212px;font-size:7.5px;line-height:10px;text-align:justify;padding-left:12px}
.item b{color:var(--blue);font-size:9.5px;font-weight:700}
.item .dot{position:absolute;left:0;top:3px;width:6px;height:6px;border-radius:50%;background:var(--yellow);border:1px solid #e0a800}
.service{width:216px;font-size:7.7px;line-height:10px;text-align:justify;padding-left:14px}
.service h3{position:relative;font-size:9.5px;font-weight:700;color:var(--blue);margin-left:-14px;padding-left:14px;margin-bottom:4px}
.service h3 svg{position:absolute;left:0;top:2px}
.adv-band{left:0;top:448px;width:516px;height:182px;background:linear-gradient(180deg,var(--sky-soft) 0%,#b9dff2 100%)}
.adv-list{font-size:7.7px;line-height:10px;text-align:justify;list-style:none}
.adv-list li{position:relative;padding-left:14px;margin-bottom:10px}
.adv-list li .n{position:absolute;left:0;top:0}
.adv-list--a{left:31px;top:462px;width:215px}
.adv-list--b{left:270px;top:462px;width:218px}
.sub{list-style:none;margin-top:4px}
.sub li{padding-left:14px;margin-bottom:5px}
</style>
</head>
<body>

<!-- FRONT -->
<section class="page page--front" aria-label="Flyer front">
  <div class="abs brand"><span class="brand__mark"></span><span class="brand__name">KLT</span></div>
  <div class="abs tagline">Reliable Utility Services</div>
  <div class="abs since">Serving Texas</div>

  <div class="abs hero-photo" role="img" aria-label="Photo of a diverse team of four professionals in blue shirts using phones and tablets around a meeting table"></div>

  <div class="abs hero-band">
    <h1>DATA PROCESSING &amp; POSTING</h1>
    <p>Helping to streamline your back office to manage work more efficiently</p>
  </div>

  <h2 class="abs intro-title"><span>Data Processing &amp; Bill Processing</span> – Managed Backoffice Administration,<br>Services That Lighten Your Work Load</h2>

  <div class="abs body-col body-col--a">
    <p>The KLT <b>Managed Backoffice Administration (MBA)</b> is here to help you manage your business effectively by systematically organizing your data and information from diverse sources, allowing you and your staff/teams to spend more time serving your customers. We convert, enter, manage, evaluate and process your data based on the individual municipality rate ordinance or per your requirement(s). With a wide range of services, we have helped companies streamline their back office and manage work more efficiently. You can rely on our extensive industry knowledge and flexible services that are cost-effective and productive.</p>
  </div>
  <div class="abs body-col body-col--b">
    <p>We have an efficient and experienced team working with a vast understanding of the various tasks involved in completing the entire billing cycle. All our representatives are friendly and knowledgeable. KLT will methodically maintain all the records and data for you, conducting processes for better client and customer relationships, bringing you maximum value.</p>
    <p>We provide you with total transparency of data. If required, we inter-connect your data so that it is easily available to your staff immediately, making interacting with customers more convenient.</p>
  </div>

  <div class="abs footer">
    <div class="abs footer__yellow"></div>
    <div class="abs footer__blue"></div>
    <div class="abs footer__phone-block"></div>
    <div class="abs footer__item" style="left:34px"><svg viewBox="0 0 10 10"><path d="M5 1 9 5H8v4H6V6H4v3H2V5H1z"/></svg>48710 Brimley Lane, Houston, TX 77093</div>
    <div class="abs footer__item" style="left:210px"><svg viewBox="0 0 10 10"><path d="M1 2h8v6H1z M1 2l4 3 4-3" fill="var(--blue)" stroke="#fff" stroke-width=".6"/></svg>sales@kltzo.com</div>
    <div class="abs footer__item" style="left:302px"><svg viewBox="0 0 10 10"><circle cx="5" cy="5" r="4"/></svg>www.kltzo.com</div>
    <div class="abs footer__phone"><svg viewBox="0 0 10 10"><path d="M2 1h2l1 2.5-1.2.8a6 6 0 0 0 2 2L6.6 5 9 6v2c0 .6-.5 1-1 1A7.5 7.5 0 0 1 1 2c0-.5.4-1 1-1z"/></svg>713-846-2059</div>
  </div>
</section>

<!-- BACK -->
<section class="page page--back" aria-label="Flyer back">
  <div class="abs section-title services-title">SERVICES <span>MBA PROVIDES:</span></div>

  <div class="abs lead"><svg class="tick" viewBox="0 0 10 10"><rect x=".5" y=".5" width="9" height="9" fill="none" stroke="var(--yellow)"/><path d="M2 5l2 2 4-5" fill="none" stroke="var(--blue)" stroke-width="1.4"/></svg>Payment channels that MBA processes:</div>

  <div class="abs channel-bar" style="top:78px">
    <span class="channel-bar__icon"></span>
    <span class="channel-bar__tab">mScan –</span>
    <span class="channel-bar__slash" style="left:86px"></span>
  </div>
  <p class="abs lockbox">Lock Box – Payments that are mailed to a secure mail box and processed in the MBA office daily Monday – Friday. All payments received each day are processed the same day.</p>

  <div class="abs channel-bar" style="top:130px">
    <span class="channel-bar__icon"></span>
    <span class="channel-bar__tab">Online Payments</span>
    <span class="channel-bar__slash" style="left:136px"></span>
  </div>

  <div class="abs grey-band"></div>
  <div class="abs item" style="left:34px;top:157px"><span class="dot"></span><b>Pack Files –</b> Payments that are made online using the billing portal/website or via telephone which can be made by check or credit card/debit card payments.</div>
  <div class="abs item" style="left:277px;top:157px"><span class="dot"></span><b>mReceivables –</b> Payments that are made by a customer using online banking or payments made at one of their local payment outlets that accepts utility payments, such as Plaza Mart, FreshWay, ValueGrocer etc.</div>
  <div class="abs item" style="left:34px;top:211px"><span class="dot"></span><b>SnapRemit</b> – Payments made using the QR Code on the customer's billing statement which allows the customer to retrieve payment information regarding their account and to make payments in a few effortless steps.</div>
  <div class="abs item" style="left:277px;top:211px"><span class="dot"></span><b>Recurring ACH/Credit Cards –</b> Customers that sign up for this service will have funds drafted from their bank account or applied to their credit card each month based on their current balance and they will not have to worry about manually making payments each month or forgetting to make a payment.</div>

  <div class="abs service" style="left:30px;top:292px">
    <h3><svg class="tick" viewBox="0 0 10 10"><rect x=".5" y=".5" width="9" height="9" fill="none" stroke="var(--yellow)"/><path d="M2 5l2 2 4-5" fill="none" stroke="var(--blue)" stroke-width="1.4"/></svg>Billing -</h3>
    MBA will process billing statements each month based on the guidance of the operator. Bills are automatically calculated based on meter reads and the rate ordinance that was provided by the operator for each of its districts.
  </div>
  <div class="abs service" style="left:274px;top:292px">
    <h3><svg class="tick" viewBox="0 0 10 10"><rect x=".5" y=".5" width="9" height="9" fill="none" stroke="var(--yellow)"/><path d="M2 5l2 2 4-5" fill="none" stroke="var(--blue)" stroke-width="1.4"/></svg>Support –</h3>
    MBA provides general support for our clients and if MBA cannot immediately resolve an issue that issue will be escalated to the next higher support level for resolution.
  </div>
  <div class="abs service" style="left:30px;top:372px">
    <h3><svg class="tick" viewBox="0 0 10 10"><rect x=".5" y=".5" width="9" height="9" fill="none" stroke="var(--yellow)"/><path d="M2 5l2 2 4-5" fill="none" stroke="var(--blue)" stroke-width="1.4"/></svg>Secured file storage of payments –</h3>
    Every payment that is processed by MBA is stored electronically for a minimum of 2 years and can be accessed for clients upon written request.
  </div>
  <div class="abs service" style="left:274px;top:372px">
    <h3><svg class="tick" viewBox="0 0 10 10"><rect x=".5" y=".5" width="9" height="9" fill="none" stroke="var(--yellow)"/><path d="M2 5l2 2 4-5" fill="none" stroke="var(--blue)" stroke-width="1.4"/></svg>Research–</h3>
    MBA provides general to complex research of payments, discrepancies, etc.
  </div>

  <div class="abs adv-band"></div>
  <div class="abs section-title adv-title">ADVANTAGES <span>OF USING MBA</span></div>

  <ol class="abs adv-list adv-list--a">
    <li><span class="n">1.</span>No learning curves to learn software. Payments and billing will be up and running immediately after conversion.</li>
    <li><span class="n">2.</span>Actual staff personnel to talk to when you have an issue.</li>
    <li><span class="n">3.</span>We have an efficient and experienced team working with a vast understanding of the various tasks involved in finalizing the billing cycle.</li>
    <li><span class="n">4.</span>Generally, more cost effective than processing payments and billing in-house.</li>
    <li><span class="n">5.</span>Deposits are usually made faster when using the MBA department versus using in-house processors.</li>
  </ol>
  <ol class="abs adv-list adv-list--b">
    <li><span class="n">6.</span>Assistance with delinquent letters and tags if requested.</li>
    <li><span class="n">7.</span>Reports to help balance bank statements.</li>
    <li><span class="n">8.</span>All payments are checked and balanced:
      <ul class="sub">
        <li>a.&nbsp; To make sure that the amount expected to be processed was processed.</li>
        <li>b.&nbsp; What was expected to go to the bank is what went to the bank.</li>
        <li>c.&nbsp; And that the bank received each payment.</li>
      </ul>
    </li>
    <li><span class="n">9.</span>Can provide customizable services depending on our client's needs.</li>
  </ol>

  <div class="abs footer">
    <div class="abs footer__yellow"></div>
    <div class="abs footer__blue"></div>
    <div class="abs footer__phone-block"></div>
    <div class="abs footer__item" style="left:34px"><svg viewBox="0 0 10 10"><path d="M5 1 9 5H8v4H6V6H4v3H2V5H1z"/></svg>48710 Brimley Lane, Houston, TX 77093</div>
    <div class="abs footer__item" style="left:210px"><svg viewBox="0 0 10 10"><path d="M1 2h8v6H1z M1 2l4 3 4-3" fill="var(--blue)" stroke="#fff" stroke-width=".6"/></svg>sales@kltzo.com</div>
    <div class="abs footer__item" style="left:302px"><svg viewBox="0 0 10 10"><circle cx="5" cy="5" r="4"/></svg>www.kltzo.com</div>
    <div class="abs footer__phone"><svg viewBox="0 0 10 10"><path d="M2 1h2l1 2.5-1.2.8a6 6 0 0 0 2 2L6.6 5 9 6v2c0 .6-.5 1-1 1A7.5 7.5 0 0 1 1 2c0-.5.4-1 1-1z"/></svg>713-846-2059</div>
  </div>
</section>

</body>
</html>
```